KORVAL RENOVATIONS AND CUSTOM BUILDS

5pages:
Home/ who we are , services offered, why us,
recent projects/ gallery , contact us

Industry/Entity Type

Design, renovations, project management

Coding

Coded - Design and coding required

Number of Pages Required

5+ page

Requirements
Should not have
• Too many colours

```html
<!DOCTYPE html>
<html lang="en">
<head>
<meta charset="utf-8">
<title>Korval Renovations and Custom Builds</title>
<link href="https://fonts.googleapis.com/css2?family=Open+Sans:ital,wght@0,300;0,400;0,600;0,700;1,600&display=swap" rel="stylesheet">
<style>
  :root {
    --navy: #2c3e55;
    --ink: #3a3a3a;
    --grey: #6b6b6b;
    --rule: #e3e3e3;
    --green: #86b83e;
    --green-deep: #74ba1c;
    --teal: #3db3a0;
    --white: #ffffff;
  }
  * { box-sizing: border-box; margin: 0; padding: 0; }
  html, body { width: 765px; height: 1200px; overflow: hidden; }
  body { position: relative; background: var(--white); font-family: "Open Sans", sans-serif; color: var(--ink); }

  .site-header { position: absolute; left: 0; top: 0; width: 765px; height: 63px; background: var(--white); border-bottom: 1px solid #d8d8d8; }
  .brand { position: absolute; left: 25px; top: 12px; display: flex; align-items: center; gap: 6px; }
  .brand-mark { width: 10px; height: 10px; background: var(--green); }
  .brand-name { font-weight: 700; font-size: 10.5px; line-height: 13px; color: var(--navy); letter-spacing: .5px; }
  .main-nav { position: absolute; top: 22px; left: 0; width: 765px; height: 18px; }
  .main-nav a { position: absolute; top: 0; font-size: 11px; font-weight: 700; letter-spacing: 1.3px; color: #333; text-decoration: none; white-space: nowrap; }
  .main-nav a.is-active { color: var(--green); }

  .hero { position: absolute; left: 0; top: 63px; width: 765px; height: 339px;
    background: linear-gradient(180deg, #1a56b8 0%, #2a4f93 40%, #7a5a3a 72%, #c38a3c 85%, #4a4a34 100%); }
  .hero-title { position: absolute; left: 0; width: 765px; top: 130px; text-align: center; color: var(--white); font-size: 36px; font-weight: 700; letter-spacing: 2px; line-height: 40px; }
  .hero-rule { position: absolute; left: 355px; top: 179px; width: 56px; height: 1px; background: var(--green); }
  .hero-sub { position: absolute; left: 0; width: 765px; top: 192px; text-align: center; color: var(--white); font-size: 14.5px; font-style: italic; font-weight: 600; letter-spacing: 1px; }
  .slider-arrow { position: absolute; left: 722px; width: 43px; height: 43px; background: rgba(220,220,220,.55); display: flex; align-items: center; justify-content: center; }

  .intro-heading { position: absolute; left: 295px; top: 446px; width: 175px; height: 55px; border-top: 1px solid var(--rule); border-bottom: 1px solid var(--rule); text-align: center; font-size: 30px; font-weight: 600; line-height: 53px; color: var(--ink); white-space: nowrap; }
  .intro-tagline { position: absolute; left: 0; width: 765px; top: 518px; text-align: center; font-size: 19px; font-weight: 600; color: #444; }

  .pull-quote { position: absolute; left: 22px; top: 599px; height: 37px; border-left: 1px solid var(--green); padding-left: 15px; font-size: 19px; line-height: 36px; color: var(--teal); }
  .section-rule { position: absolute; left: 22px; top: 655px; width: 352px; height: 1px; background: var(--rule); }
  .about-copy { position: absolute; left: 22px; top: 673px; width: 355px; font-size: 10.6px; line-height: 22.4px; font-weight: 400; color: var(--grey); }

  .feature-frame { position: absolute; left: 392px; top: 599px; width: 351px; height: 225px; border: 8px solid var(--teal); background: var(--white); }
  .feature-art { width: 100%; height: 100%; background: radial-gradient(ellipse at 55% 50%, #dfe3e8 0%, #f2f3f5 55%, #ffffff 100%); }

  .site-footer { position: absolute; left: 0; top: 868px; width: 765px; height: 290px; background: var(--green); color: var(--white); }
  .footer-brand { position: absolute; left: 22px; top: 43px; width: 114px; height: 61px; background: var(--white); border: 2px solid var(--teal); display: flex; align-items: center; justify-content: center; gap: 5px; }
  .footer-col { position: absolute; top: 42px; }
  .footer-col h3 { font-size: 12.5px; font-weight: 600; }
  .footer-links { list-style: none; margin-top: 10px; }
  .footer-links li { font-size: 10px; line-height: 24.6px; }
  .contact-list { list-style: none; margin-top: 23px; }
  .contact-list li { font-size: 10px; line-height: 23px; }
  .social { position: absolute; left: 515px; top: 188px; display: flex; gap: 7.5px; }
  .social span { width: 22px; height: 22px; border-radius: 50%; display: block; }
  .to-top { position: absolute; left: 736px; }

  .copyright-bar { position: absolute; left: 0; top: 1158px; width: 765px; height: 42px; background: var(--green-deep); color: var(--white); text-align: center; font-size: 6px; font-weight: 700; line-height: 42px; }
</style>
</head>
<body>
  <header class="site-header">
    <div class="brand">
      <span class="brand-mark"></span>
      <div class="brand-name">KORVAL<br>RENOVATIONS<br>AND CUSTOM BUILDS</div>
    </div>
    <nav class="main-nav">
      <a class="is-active" style="left:315px">HOME</a>
      <a style="left:370px">ABOUT US</a>
      <a style="left:451px">SERVICES</a>
      <a style="left:527px">RECENT PROJECTS</a>
      <a style="left:655px">CONTACT US</a>
    </nav>
  </header>

  <section class="hero" role="img" aria-label="Photo of a lit two-storey house at dusk with blossoming tree">
    <h1 class="hero-title">KORVAL</h1>
    <div class="hero-rule"></div>
    <p class="hero-sub">RENOVATIONS AND CUSTOM BUILDS</p>
    <div class="slider-arrow" style="top:127px"><svg width="10" height="16" viewBox="0 0 10 16"><path d="M8 1 L2 8 L8 15" fill="none" stroke="#444" stroke-width="1"/></svg></div>
    <div class="slider-arrow" style="top:171px"><svg width="10" height="16" viewBox="0 0 10 16"><path d="M2 1 L8 8 L2 15" fill="none" stroke="#444" stroke-width="1"/></svg></div>
  </section>

  <h2 class="intro-heading">Who We Are</h2>
  <p class="intro-tagline">Dedication, experience and a passion for perfection.</p>

  <p class="pull-quote">We build great homes.</p>
  <div class="section-rule"></div>
  <p class="about-copy">Our desire to work closely with those who share the same vision and values is why many of our clients have a multiple project history. Exceeding client expectations has resulted in continual repeat business within the local area, which means we are building a foundation not only for our business but also for our community.</p>

  <div class="feature-frame">
    <div class="feature-art" role="img" aria-label="Sketch of a house being framed by two hands"></div>
  </div>
  <svg class="to-top" style="top:706px" width="14" height="8" viewBox="0 0 14 8"><path d="M1 7 L7 1 L13 7" fill="none" stroke="#999" stroke-width="1"/></svg>

  <footer class="site-footer">
    <div class="footer-brand">
      <span class="brand-mark"></span>
      <span class="brand-name">KORVAL<br>RENOVATIONS<br>AND CUSTOM BUILDS</span>
    </div>
    <div class="footer-col" style="left:269px">
      <h3>Company</h3>
      <ul class="footer-links">
        <li>Home</li><li>About Us</li><li>Services</li><li>Recent Projects</li><li>Contact Us</li>
      </ul>
    </div>
    <div class="footer-col" style="left:515px">
      <h3>Contact Us</h3>
      <ul class="contact-list">
        <li>Phone :#5550142</li>
        <li>Email: info@korval.com</li>
        <li>Address: Birchwood Street Canada</li>
      </ul>
    </div>
    <div class="social" aria-label="Social links">
      <span style="background:#1877f2"></span>
      <span style="background:#1da1f2"></span>
      <span style="background:#0a66c2"></span>
      <span style="background:#e1306c"></span>
    </div>
    <svg class="to-top" style="top:56px" width="14" height="8" viewBox="0 0 14 8"><path d="M1 7 L7 1 L13 7" fill="none" stroke="#c7dca5" stroke-width="1"/></svg>
  </footer>

  <div class="copyright-bar">COPYRIGHT 2018 - ALL RIGHTS RESERVED.</div>
  <svg class="to-top" style="top:1176px" width="14" height="8" viewBox="0 0 14 8"><path d="M1 7 L7 1 L13 7" fill="none" stroke="#b9dc8c" stroke-width="1"/></svg>
</body>
</html>
```